Creative Graphic Designer needed to create fabulous wash cloths

We are an Interior design business and are releasing a range of wash cloths.
We would like some innovative designs to have screen printed on these cloths.
We will only be printing on one side.

The size of the cloth is 18 cm x 20 cm and the colour of the cloth is variable.

At this stage we have selected white, turquoise, orange and apple green as the base colours we require. (see attached)

1. The first design should portray 'used for washing up' and
2. the second 'used for wiping around'. Or just 'wiping only' sink only.

These can be in image format or a combination of image and text.

I am happy for you to use the whole of the cloth, or as little as you see fit.

I would see two print colours or max three, onto the base cloth.

I have also attached our company logo which I would like incorporated somewhere on the cloth, it can be as small or large as you like.
We are looking for something really creative.

Thanks so much!

Target Market(s)

Medium to high end

Industry/Entity Type

Graphic Designer

Requirements
Must have
• include the logo somewhere on the wash cloth. Final design must be in .eps or pdf. and PANTONE colours.
Nice to have
• Something really fun and creative, however we are looking for originality
• I have included some concepts previously done to show what can be done.
• I dont mind if they are images, scenes, text, whatever you feel portrays the 'use for in the sink' and use for wiping around best.
• The attached image of New York I particularly like, I understand it has used alot more colours, but I found the concept really nice.
Should not have
• More than three colours.

```html
<!DOCTYPE html>
<html lang="en">
<head>
<meta charset="utf-8">
<title>Used for Washing Up – Wash Cloth</title>
<link href="https://fonts.googleapis.com/css2?family=Josefin+Sans:wght@600;700&display=swap" rel="stylesheet">
<style>
  :root {
    --cloth-turquoise: #24b3b8;
    --ink-black: #121414;
    --deep-teal: #1b4a4b;
    --rim-teal: #17686a;
  }
  html, body {
    margin: 0;
    padding: 0;
    width: 1080px;
    height: 1200px;
    overflow: hidden;
    background: var(--cloth-turquoise);
  }
  .cloth {
    display: block;
    width: 1080px;
    height: 1200px;
  }
  .cloth-base { fill: var(--cloth-turquoise); }
  .slogan {
    font-family: "Josefin Sans", "Futura", sans-serif;
    font-weight: 600;
    fill: var(--ink-black);
  }
  .sponge-letter { fill: var(--deep-teal); }
  .plate-letter { fill: url(#plate-tone); }
  .brand-name {
    font-family: "Josefin Sans", "Futura", sans-serif;
    font-weight: 600;
    font-size: 50px;
    fill: var(--ink-black);
  }
  .brand-square { fill: var(--ink-black); }
</style>
</head>
<body>
<svg class="cloth" viewBox="0 0 1080 1200" xmlns="http://www.w3.org/2000/svg">
  <defs>
    <radialGradient id="plate-tone" cx="50%" cy="50%" r="50%">
      <stop offset="0%" stop-color="#1b4a4b"/>
      <stop offset="70%" stop-color="#1b4a4b"/>
      <stop offset="100%" stop-color="#17686a"/>
    </radialGradient>
  </defs>

  <rect class="cloth-base" x="0" y="0" width="1080" height="1200"/>

  <!-- Line 1: USE + sponge letter D -->
  <text class="slogan" x="16" y="277" font-size="272" textLength="424" lengthAdjust="spacingAndGlyphs">USE</text>
  <rect class="sponge-letter" x="454" y="25" width="136" height="257" rx="60"
        role="img" aria-label="Scrubbing sponge shaped as the letter D with a hanging loop"/>

  <!-- Line 2: F + plate letter O + R -->
  <text class="slogan" x="16" y="552" font-size="246" textLength="107" lengthAdjust="spacingAndGlyphs">F</text>
  <ellipse class="plate-letter" cx="227" cy="458" rx="92" ry="102"
           role="img" aria-label="Dinner plate seen from above, standing in for the letter O"/>
  <text class="slogan" x="331" y="552" font-size="246" textLength="120" lengthAdjust="spacingAndGlyphs">R</text>

  <!-- Line 3 -->
  <text class="slogan" x="16" y="835" font-size="246" textLength="1036" lengthAdjust="spacingAndGlyphs">WASHING</text>

  <!-- Line 4 -->
  <text class="slogan" x="16" y="1117" font-size="246" textLength="284" lengthAdjust="spacingAndGlyphs">UP</text>

  <!-- Brand sign-off -->
  <g class="brand">
    <rect class="brand-square" x="838" y="1068" width="30" height="30"/>
    <text class="brand-name" x="882" y="1102" textLength="168" lengthAdjust="spacing">VERRA</text>
  </g>
</svg>
</body>
</html>
```